Screen Tides - Report on digital habits and attitudes

We are a research company and we have written a PowerPoint Report to present the results of a series of surveys conducted in the last three years. The research is about the "Screen Tides": people are facing the opportunities and challanges of their lives transformed by the digital technologies. We have investigated a number of topics through thousands of interviews and we've analyzed the data presented in the PowerPoint document.
We're not quite satisfied with the look and feel of the report: it looks too flat and boring, too "basic" to be presented as a professional work, yet being just that. We'd like you to upgrade the graphics and style of the report up to the level of a professional research product. The document still needs to be fully editable (either text and charts) but you can rearrange all the contents as you please, adding images, changing font and text size, colors and whatever you think is necessary to reach our goal.

Target Market(s)

Media covering digital issues
Marketing executives
Public institutions and policy makers

Industry/Entity Type

Market Research

Requirements
Must have
• The treats of a professional work
Fully editable within PowerPoint (either text and charts)
Nice to have
• Smart images
Original organization of the pages
Colors and graphics coherent with the corvalmeadow.it logo/website look and feel
Should not have
• PPT document over 30 MBytes
Images violating copyright

```html
<!DOCTYPE html>
<html lang="it">
<head>
<meta charset="utf-8">
<title>Osservatorio Screen Tides – Report</title>
<link rel="stylesheet" href="https://fonts.googleapis.com/css2?family=Barlow:wght@400;600;700&family=Comfortaa:wght@700&display=swap">
<style>
:root{
  --canvas:#d9d9d9;
  --orange:#f39324;
  --orange-soft:#f9b66a;
  --peach:#fdebd8;
  --navy:#1f3d8a;
  --index-blue:#2c4e9e;
  --maroon:#8e1b3e;
  --purple:#5b4a9b;
  --purple-soft:#a79fd0;
  --lavender:#e9e6f4;
  --ice:#e2e8f5;
  --blue-soft:#7f93cb;
  --ink:#3a3a3a;
  --muted:#8a8a8a;
  --footer:#a4a4a4;
  --white:#ffffff;
}
*{box-sizing:border-box;margin:0;padding:0}
html,body{width:1200px;height:3623px;overflow:hidden}
body{background:var(--canvas);font-family:"Barlow",sans-serif;color:var(--ink);position:relative}
.page{position:absolute;width:491px;height:635px;background:var(--white);overflow:hidden}
.text{font-size:6.4px;line-height:1.38;text-align:justify;color:var(--ink)}
.text p+p{margin-top:5px}
.text b{font-weight:700}
.abs{position:absolute}
.cover-title{font-family:"Barlow",sans-serif;font-weight:700;font-size:34px;color:var(--navy);line-height:1.05;text-align:center}
.page-head{position:absolute;left:0;top:14px;display:flex;align-items:center}
.head-icon{width:36px;height:34px;display:flex;align-items:center;justify-content:center}
.head-title{font-family:"Comfortaa",sans-serif;font-weight:700;font-size:31px;margin-left:12px;letter-spacing:-.3px}
.brand-mark{position:absolute;top:14px;right:14px;display:flex;align-items:center;gap:3px;font-size:6px;font-weight:600;color:var(--orange)}
.brand-mark i{width:9px;height:9px;border-radius:50%;background:var(--orange);display:block}
.page-foot{position:absolute;left:0;right:0;bottom:0;height:14px;background:var(--footer);color:var(--white);font-size:6px;display:flex;align-items:center;padding-left:22px}
.page-num{position:absolute;right:0;top:0;height:14px;width:62px;display:flex;align-items:center;justify-content:center;font-size:6px}
.banner{position:absolute;left:24px;right:24px;height:15px;color:var(--white);font-weight:700;font-size:9px;display:flex;align-items:center;justify-content:center}
.note{font-size:4.8px;color:var(--muted);font-style:italic;text-align:center}
.bars{position:absolute;left:24px;right:24px}
.bar-row{display:flex;align-items:center;height:9.2px}
.bar-label{width:58%;text-align:right;font-size:5px;padding-right:4px;white-space:nowrap;overflow:hidden;color:#555}
.bar-track{width:42%}
.bar{height:7px;color:var(--white);font-size:5.3px;text-align:right;padding-right:3px;line-height:7px}
.chart-label{font-family:"Barlow",sans-serif;font-size:8px;fill:#555}
.axis-label{font-family:"Barlow",sans-serif;font-size:7.5px;fill:#777}
.sub-chart-title{font-size:6.4px;text-align:center;border-bottom:1px solid #ccc;padding-bottom:2px}
</style>
</head>
<body>

<!-- ===== Cover ===== -->
<section class="page" style="left:83px;top:127px">
  <div class="abs" style="left:0;right:0;top:0;height:8px;background:var(--orange)"></div>
  <div class="abs" style="left:0;right:0;top:8px;height:125px;display:flex;align-items:center;justify-content:center;padding:0 20px">
    <h1 class="cover-title">OST<br>Osservatorio Screen Tides</h1>
  </div>
  <div class="abs" role="img" aria-label="Mano che sostiene un globo luminoso di rete digitale circondato da icone di comunicazione su sfondo blu" style="left:0;right:0;top:133px;height:494px;background:radial-gradient(circle at 52% 45%,#c9e8ff 0,#5aa2e6 14%,#1f5fb8 36%,#123f86 62%,#0b2b63 100%)"></div>
  <div class="abs" style="left:0;right:0;bottom:0;height:8px;background:var(--navy)"></div>
  <div class="abs" style="left:221px;top:555px;width:50px;height:56px;background:var(--white);display:flex;flex-direction:column;align-items:center;justify-content:center;gap:4px">
    <i style="width:12px;height:12px;border-radius:50%;background:var(--orange);display:block"></i>
    <span style="font-size:5px;font-weight:700;color:var(--navy);text-align:center;line-height:1.1">CORVAL<br>MEADOW</span>
  </div>
</section>

<!-- ===== Indice ===== -->
<section class="page" style="left:634px;top:127px;background:var(--index-blue)">
  <div class="abs" style="left:0;top:20px;width:125px;height:16px;background:var(--orange)"></div>
  <div class="abs" style="right:0;top:0;width:40px;height:635px;background:linear-gradient(180deg,#1b3a80,#2c4e9e 40%,#2c4e9e)"></div>
  <div class="abs" style="left:40px;top:100px;font-family:'Comfortaa',sans-serif;font-weight:700;font-size:52px;color:var(--white)">Indice</div>
  <ul class="abs" style="left:40px;top:178px;list-style:none;color:var(--white);font-size:15px;line-height:32.5px;width:300px">
    <li><span style="color:var(--orange)">●</span> Capitolo 1 ....................................... <span style="float:right">1</span></li>
    <li><span style="color:var(--orange)">●</span> Capitolo 1 ....................................... <span style="float:right">4</span></li>
    <li><span style="color:var(--orange)">●</span> Capitolo 1 ....................................... <span style="float:right">10</span></li>
    <li><span style="color:var(--orange)">●</span> Capitolo 1 ....................................... <span style="float:right">15</span></li>
    <li><span style="color:var(--orange)">●</span> Capitolo 1 ....................................... <span style="float:right">20</span></li>
    <li><span style="color:var(--orange)">●</span> Capitolo 1 ....................................... <span style="float:right">24</span></li>
    <li><span style="color:var(--orange)">●</span> Capitolo 1 ....................................... <span style="float:right">28</span></li>
  </ul>
  <div class="abs" style="left:40px;top:560px;display:flex;align-items:center;gap:4px;color:var(--orange);font-size:8px;font-weight:600"><i style="width:12px;height:12px;border-radius:50%;background:var(--orange);display:block"></i>Corval Meadow</div>
</section>

<!-- ===== Introduzione ===== -->
<section class="page" style="left:83px;top:802px">
  <div class="abs" role="img" aria-label="Motivo decorativo di rete digitale blu" style="left:0;top:0;width:58px;height:265px;background:linear-gradient(180deg,#0d2a66,#1f5cb0 55%,rgba(255,255,255,0))"></div>
  <div class="brand-mark"><i></i>Corval Meadow</div>
  <div class="abs" style="left:120px;top:68px;font-family:'Comfortaa',sans-serif;font-weight:700;font-size:30px;color:var(--orange)">Introduzione</div>
  <div class="abs text" style="left:120px;right:24px;top:125px">
    <p>Il digitale ha cambiato il mondo a un livello di profondità di cui non siamo ancora pienamente consapevoli. È facile riconoscere le manifestazioni del digitale nei <b>comportamenti delle persone</b> e notare come ha formato nuove abitudini e ritualità quotidiane. Non è altrettanto immediato comprendere quanto il digitale abbia modificato il <b>mondo interiore</b> e abbia inciso sul senso dell'identità, sulle emozioni in gioco nelle relazioni, su affetti e sessualità, sul modo di concepire la società, i diritti e la libertà personale.</p>
    <p>L'obiettivo di questo lavoro di ricerca è raccontare la struttura e l'evoluzione di alcuni atteggiamenti di fondo che influenzano i comportamenti quotidiani legati alle tecnologie digitali. Le informazioni sono ricavate dalle dichiarazioni di campioni di individui chiamati a riflettere sull'<b>ambiente connesso</b>, cioè l'insieme di tutte le relazioni e attività che si possono svolgere grazie alla Rete e, più in generale, grazie a tutte le innovazioni introdotte dagli strumenti e dai servizi digitali.</p>
  </div>
  <div class="abs text" style="left:24px;right:24px;top:300px">
    <p>L'analisi indaga le dinamiche cognitive e psicologiche che originano i comportamenti e descrive gli orientamenti di base sottostanti alle scelte – talvolta inconsapevoli – che danno forma alla dimensione digitale della vita. Questa, infatti, può assumere una configurazione molto diversa dalla dimensione della vita di prima (a cui ci riferiamo col termine «naturale»), intendendo con questo la vita non mediata dagli strumenti dell'ICT): persone introverse nella vita naturale possono avere una vita digitale ricca di relazioni e, allo stesso modo, così come persone di orientamento liberale nella vita naturale possono assumere atteggiamenti rezionari o anarchici nella dimensione digitale della vita.</p>
    <p>La recente esperienza del lockdown per il Covid-19 ha <b>accelerato l'evoluzione del fenomeno</b> e ha esasperato alcuni aspetti della <b>dimensione digitale della vita</b>. Per alcuni mesi il mondo è stato un inedito e prezioso laboratorio di psicologia sociale: le forme digitali delle relazioni personali e sociali hanno prevalso e sostituito quelle della vita naturale e hanno generato riflessioni non astratte ma elaborate sulla base delle esperienze vissute. Per questo motivi Corval Meadow ha prodotto le analisi dei dati e ha anticipato l'uscita di questo Rapporto, anche se il lavoro ha l'obiettivo di seguire i fenomeni per un tempo più lungo, di almeno un decennio.</p>
    <p>Le innovazioni dell'epoca moderna hanno generato benessere diffuso: dalla medicina all'elettricità, dalla diffusione della conoscenza alla produzione e distribuzione dei prodotti alimentari. La domanda che ci poniamo oggi è relativa alle tecnologie digitali: ci renderanno la vita più facile, la convivenza più pacifica, ci daranno una salute migliore?</p>
  </div>
  <div class="abs" style="left:24px;top:552px;font-size:10px;font-weight:700;color:var(--navy)">In definitiva, il digitale ci renderà più felici?</div>
  <div class="page-foot">La dimensione digitale della vita | DICEMBRE 2021 | @CorvalMeadow2021<div class="page-num" style="background:var(--orange-soft)">PAGE 1</div></div>
</section>

<!-- ===== La Ricerca ===== -->
<section class="page" style="left:634px;top:802px">
  <div class="page-head">
    <div class="head-icon" style="background:var(--maroon)"><svg width="18" height="18" viewBox="0 0 18 18"><circle cx="7" cy="7" r="5" fill="none" stroke="#fff" stroke-width="2.2"/><line x1="11" y1="11" x2="16" y2="16" stroke="#fff" stroke-width="2.6" stroke-linecap="round"/></svg></div>
    <div class="head-title" style="color:var(--maroon)">La Ricerca</div>
  </div>
  <div class="brand-mark"><i></i>Corval Meadow</div>
  <div class="abs text" style="left:24px;right:24px;top:85px">
    <p>"L'ambiente connesso è tutto ciò che accade perché siamo connessi alla rete: tutti i modi che, grazie alla connessione alla rete, abbiamo per comunicare con altre persone e tessere relazioni, per fruire di contenuti di tutti i tipi (informazioni testuali, video, musica, giochi etc), per acquistare prodotti e utilizzare servizi (bancari, amministrativi, pagamenti), o utilizzare nuove tecnologie per la casa, per la mobilità, per il fitness e la salute, etc… Alcune di queste attività fanno ormai parte della nostra vita quotidiana, altre probabilmente lo diventeranno nei prossimi anni. Ecco, tutto questo compone l'ambiente connesso.</p>
    <p>La popolazione online riesce quindi a rappresentare quella fetta di società italiana maggiormente impattata dal fenomeno della digitalizzazione e del mondo connesso, anche se con livelli di consapevolezza, stress, paure e atteggiamenti completamente diversi che descrivono «mondi» molto diversi.</p>
    <p>L'esigenza di capire il vissuto degli italiani su questi temi è nata in Corval Meadow nel 2018 e si è concretizzata con la prima rilevazione a Gennaio 2019, momento in cui si è «fotografata» per la prima volta la situazione. Poiché il fenomeno descritto è in continua evoluzione e cambiamento, si è scelto di monitorarlo con una rilevazione semestrale ma l'emergenza Covid-19 ha reso necessario</p>
  </div>
  <div class="abs" style="left:24px;right:24px;top:302px;height:42px;border:1px solid var(--maroon);padding:4px 6px">
    <div style="font-size:5px;text-align:center;color:#555">Analisi di 27 aspetti dell'impatto del digitale nella vita quotidiana: interviste a un campione di popolazione maggiorenne</div>
    <div style="display:flex;gap:1.5px;justify-content:center;margin-top:3px">
      <span style="display:flex;gap:1.5px"><i style="width:9px;height:9px;background:#7a9bd3;display:block"></i><i style="width:9px;height:9px;background:#7a9bd3;display:block"></i><i style="width:9px;height:9px;background:#7a9bd3;display:block"></i><i style="width:9px;height:9px;background:#7a9bd3;display:block"></i><i style="width:9px;height:9px;background:#7a9bd3;display:block"></i><i style="width:9px;height:9px;background:#7a9bd3;display:block"></i><i style="width:9px;height:9px;background:#7a9bd3;display:block"></i><i style="width:9px;height:9px;background:#7a9bd3;display:block"></i></span>
      <span style="display:flex;gap:1.5px"><i style="width:9px;height:9px;background:#8cc063;display:block"></i><i style="width:9px;height:9px;background:#8cc063;display:block"></i><i style="width:9px;height:9px;background:#8cc063;display:block"></i><i style="width:9px;height:9px;background:#8cc063;display:block"></i><i style="width:9px;height:9px;background:#8cc063;display:block"></i><i style="width:9px;height:9px;background:#8cc063;display:block"></i><i style="width:9px;height:9px;background:#8cc063;display:block"></i><i style="width:9px;height:9px;background:#8cc063;display:block"></i></span>
      <span style="display:flex;gap:1.5px"><i style="width:9px;height:9px;background:#5bb6c9;display:block"></i><i style="width:9px;height:9px;background:#5bb6c9;display:block"></i><i style="width:9px;height:9px;background:#5bb6c9;display:block"></i><i style="width:9px;height:9px;background:#5bb6c9;display:block"></i><i style="width:9px;height:9px;background:#5bb6c9;display:block"></i><i style="width:9px;height:9px;background:#5bb6c9;display:block"></i><i style="width:9px;height:9px;background:#5bb6c9;display:block"></i></span>
      <span style="display:flex;gap:1.5px"><i style="width:9px;height:9px;background:#f2b35a;display:block"></i><i style="width:9px;height:9px;background:#f2b35a;display:block"></i><i style="width:9px;height:9px;background:#f2b35a;display:block"></i><i style="width:9px;height:9px;background:#f2b35a;display:block"></i><i style="width:9px;height:9px;background:#f2b35a;display:block"></i><i style="width:9px;height:9px;background:#f2b35a;display:block"></i><i style="width:9px;height:9px;background:#f2b35a;display:block"></i></span>
      <span style="display:flex;gap:1.5px"><i style="width:9px;height:9px;background:#e07a7a;display:block"></i><i style="width:9px;height:9px;background:#e07a7a;display:block"></i><i style="width:9px;height:9px;background:#e07a7a;display:block"></i><i style="width:9px;height:9px;background:#e07a7a;display:block"></i><i style="width:9px;height:9px;background:#e07a7a;display:block"></i><i style="width:9px;height:9px;background:#e07a7a;display:block"></i><i style="width:9px;height:9px;background:#e07a7a;display:block"></i></span>
    </div>
    <div style="display:flex;justify-content:space-around;font-size:4.8px;margin-top:2px;font-weight:600">
      <span style="color:#4d72b8">8 domande sulle paure</span><span style="color:#6ea441">8 domande sulle speranze</span><span style="color:#3a9ab0">7 di atteggiamento</span><span style="color:#e09a3a">7 su Data&amp;Privacy</span><span style="color:#c95b5b">7 sulla società digitale</span>
    </div>
  </div>
  <div class="abs" style="left:0;right:0;top:352px;bottom:14px;background:var(--maroon)"></div>
  <div class="abs text" style="left:24px;width:212px;top:362px;color:var(--white)">
    <p>"L'ambiente connesso è tutto ciò che accade perché siamo connessi alla rete: tutti i modi che, grazie alla connessione alla rete, abbiamo per comunicare con altre persone e tessere relazioni, per fruire di contenuti di tutti i tipi (informazioni testuali, video, musica, giochi etc), per acquistare prodotti e utilizzare servizi (bancari, amministrativi, pagamenti), o utilizzare nuove tecnologie per la casa, per la mobilità, per il fitness e la salute, etc… Alcune di queste attività fanno ormai parte della nostra vita quotidiana, altre probabilmente lo diventeranno nei prossimi anni. Ecco, tutto questo compone l'ambiente connesso.</p>
  </div>
  <div class="abs text" style="left:255px;right:24px;top:362px;color:var(--white)">
    <p>La popolazione online riesce quindi a rappresentare quella fetta di società italiana maggiormente impattata dal fenomeno della digitalizzazione e del mondo connesso, anche se con livelli di consapevolezza, stress, paure e atteggiamenti completamente diversi che descrivono «mondi» molto diversi.</p>
    <p>L'esigenza di capire il vissuto degli italiani su questi temi è nata in Corval Meadow nel 2018 e si è concretizzata con la prima rilevazione a Gennaio 2019, momento in cui si è «fotografata» per la prima volta la situazione. Poiché il fenomeno descritto è in continua evoluzione e cambiamento, si è scelto di monitorarlo con una rilevazione semestrale ma l'emergenza Covid-19 ha reso necessario</p>
  </div>
  <div class="page-foot">La dimensione digitale della vita | DICEMBRE 2021 | @CorvalMeadow2021<div class="page-num" style="background:#c4162f">PAGE 2</div></div>
</section>

<!-- ===== Le Paure 1 ===== -->
<section class="page" style="left:83px;top:1514px">
  <div class="page-head">
    <div class="head-icon" style="background:var(--purple)"><svg width="20" height="18" viewBox="0 0 20 18"><polygon points="10,1 19,17 1,17" fill="#fff"/><rect x="9" y="6" width="2" height="6" fill="#5b4a9b"/><rect x="9" y="13.5" width="2" height="2" fill="#5b4a9b"/></svg></div>
    <div class="head-title" style="color:var(--purple)">Le Paure</div>
  </div>
  <div class="brand-mark"><i></i>Corval Meadow</div>
  <div class="abs text" style="left:24px;right:24px;top:62px">
    <p>Il digitale può fare paura per le conseguenze che produce nelle capacità cognitive, nelle relazioni personali e sociali, fino a quelle internazionali. Molti non conoscono cosa c'è dietro e da dove vengono certe <b>magie della tecnologia</b>, alle quali ci siamo abituati e che non ci meravigliano più ma rimangono in gran parte incomprensibili. Inoltre, certi racconti sulle sorveglianza digitale e sui nuovi poteri che emergono dai dati ispirano un senso di sospetto condiviso da un'ampia maggioranza di individui.</p>
  </div>
  <div class="banner" style="top:128px;background:var(--purple-soft)">Le paure e i sospetti</div>
  <div class="bars" style="top:150px">
    <div class="bar-row"><div class="bar-label">Nell'ambiente connesso è più facile manipolare le persone</div><div class="bar-track"><div class="bar" style="width:80%;background:var(--purple)">80%</div></div></div>
    <div class="bar-row"><div class="bar-label">I ragazzi hanno notevoli problemi di socializzazione a causa del digitale</div><div class="bar-track"><div class="bar" style="width:77%;background:var(--purple)">77%</div></div></div>
    <div class="bar-row"><div class="bar-label">Alcuni servizi sanno tutto di noi: chi vediamo, cosa facciamo, cosa scriviamo e…</div><div class="bar-track"><div class="bar" style="width:75%;background:var(--purple)">75%</div></div></div>
    <div class="bar-row"><div class="bar-label">I dispositivi che utilizzo mandano continuamente dati su di me a organizzazioni…</div><div class="bar-track"><div class="bar" style="width:71%;background:var(--purple-soft)">71%</div></div></div>
    <div class="bar-row"><div class="bar-label">Le notizie online ci fanno perdere la capacità di distinguere il vero dal falso</div><div class="bar-track"><div class="bar" style="width:70%;background:var(--purple-soft)">70%</div></div></div>
    <div class="bar-row"><div class="bar-label">Il digitale diminuisce la capacità di apprendimento e tutte le età</div><div class="bar-track"><div class="bar" style="width:42%;background:var(--purple-soft)">42%</div></div></div>
    <div class="bar-row"><div class="bar-label">Le democrazie sono a rischio a causa della diffusione del digitale online</div><div class="bar-track"><div class="bar" style="width:35%;background:var(--purple-soft)">35%</div></div></div>
    <div class="bar-row"><div class="bar-label">Prossimamente ci sarà una guerra cibernetica fra Stati</div><div class="bar-track"><div class="bar" style="width:33%;background:var(--purple-soft)">33%</div></div></div>
  </div>
  <div class="abs note" style="left:24px;right:24px;top:230px">Incidenza sul totale campione dei Top2Box di accordo, in una scala a 5 passi (1.017 casi a novembre 2020)</div>
  <div class="abs" style="left:24px;right:24px;top:250px;height:338px;background:var(--lavender)"></div>
  <div class="abs text" style="left:34px;right:34px;top:258px">
    <p>Il sospetto che il flusso di informazioni generato dalle tecnologie sia utilizzato con finalità di <b>controllo e manipolazione</b> è molto diffuso e riguarda otto individui sui dieci; il 75% si dichiara d'accordo con l'affermazione secondo la quale il digitale crea <b>problemi di socialità</b> nei ragazzi e il dato aumenta tra le persone oltre i 54 anni di età. Così come tra i meno giovani trova conferma l'idea, già piuttosto diffusa, che il digitale diminuisca le <b>capacità di apprendimento</b>. Le paure sulle conseguenze politiche e sociali del digitale sono più contenute ma riguardano pur sempre un terzo della popolazione.</p>
  </div>
  <div class="banner" style="top:319px;left:24px;right:24px;background:var(--purple-soft);height:17px;font-size:10px">Il trend dell'indice di paura</div>
  <svg class="abs" style="left:34px;top:345px" width="423" height="230" viewBox="0 0 423 230">
    <polyline points="40,120 110,104 190,52 275,92 360,92" fill="none" stroke="#777" stroke-width="1.4" stroke-dasharray="1.5 3" stroke-linecap="round"/>
    <g fill="#777"><circle cx="40" cy="120" r="2"/><circle cx="110" cy="104" r="2"/><circle cx="190" cy="52" r="2"/><circle cx="275" cy="92" r="2"/><circle cx="360" cy="92" r="2"/></g>
    <text class="chart-label" x="30" y="140">58%</text><text class="chart-label" x="103" y="120">59%</text><text class="chart-label" x="180" y="45">62%</text><text class="chart-label" x="268" y="110">60%</text><text class="chart-label" x="352" y="85">60%</text>
    <text class="axis-label" x="28" y="195">feb 19</text><text class="axis-label" x="100" y="195">ott 19</text><text class="axis-label" x="178" y="195">feb 20</text><text class="axis-label" x="262" y="195">mag 20</text><text class="axis-label" x="348" y="195">nov 20</text>
    <line x1="15" y1="180" x2="408" y2="180" stroke="#ccc" stroke-width=".6"/>
  </svg>
  <div class="abs note" style="left:24px;right:24px;top:557px">L'indice di paura è ottenuto come media semplice dei Top2Box delle otto voci analizzate</div>
  <div class="page-foot">La dimensione digitale della vita | DICEMBRE 2021 | @CorvalMeadow2021<div class="page-num" style="background:var(--purple-soft)">PAGE 3</div></div>
</section>

<!-- ===== Le Paure 2 ===== -->
<section class="page" style="left:634px;top:1514px">
  <div class="page-head">
    <div class="head-icon" style="background:var(--purple)"><svg width="20" height="18" viewBox="0 0 20 18"><polygon points="10,1 19,17 1,17" fill="#fff"/><rect x="9" y="6" width="2" height="6" fill="#5b4a9b"/><rect x="9" y="13.5" width="2" height="2" fill="#5b4a9b"/></svg></div>
    <div class="head-title" style="color:var(--purple)">Le Paure</div>
  </div>
  <div class="brand-mark"><i></i>Corval Meadow</div>
  <div class="abs text" style="left:24px;width:212px;top:62px">
    <p>Otto persone su dieci ritengono che nell'ambiente digitale si siano diffuse <b>pratiche di manipolazione</b> delle persone più efficaci rispetto al passato. Il riferimento al passato è relativo al '900, epoca in cui i mezzi di comunicazione di massa, tutti broadcasting, erano gestiti dai governi e dai grandi editori.</p>
  </div>
  <div class="banner" style="top:124px;left:24px;right:255px;background:var(--purple-soft)">La manipolazione delle persone</div>
  <svg class="abs" style="left:24px;top:142px" width="212" height="90" viewBox="0 0 212 90">
    <polyline points="20,42 62,52 106,66 150,42 190,34" fill="none" stroke="#777" stroke-width="1.2" stroke-dasharray="1.5 3" stroke-linecap="round"/>
    <text class="chart-label" x="8" y="36">79%</text><text class="chart-label" x="52" y="66">78%</text><text class="chart-label" x="96" y="80">77%</text><text class="chart-label" x="140" y="36">79%</text><text class="chart-label" x="178" y="28">80%</text>
    <text class="axis-label" x="10" y="88" style="font-size:6.5px">feb 19</text><text class="axis-label" x="50" y="88" style="font-size:6.5px">ott 19</text><text class="axis-label" x="92" y="88" style="font-size:6.5px">feb 20</text><text class="axis-label" x="134" y="88" style="font-size:6.5px">mag 20</text><text class="axis-label" x="176" y="88" style="font-size:6.5px">nov 20</text>
  </svg>
  <div class="abs text" style="left:24px;width:212px;top:240px">
    <p>Il sospetto sulla facilità di manipolazione delle persone è molto stabile e non si rileva alcuna tendenza significativa in tutto il periodo considerato.</p>
  </div>
  <div class="banner" style="top:280px;left:24px;right:255px;background:var(--purple-soft)">Socialità e rapporti umani</div>
  <svg class="abs" style="left:24px;top:298px" width="212" height="125" viewBox="0 0 212 125">
    <polyline points="20,38 62,52 106,38 150,82 190,36" fill="none" stroke="#777" stroke-width="1.2" stroke-dasharray="1.5 3" stroke-linecap="round"/>
    <text class="chart-label" x="8" y="32">77%</text><text class="chart-label" x="52" y="66">75%</text><text class="chart-label" x="96" y="32">77%</text><text class="chart-label" x="142" y="96">72%</text><text class="chart-label" x="178" y="28">77%</text>
    <text class="axis-label" x="10" y="120" style="font-size:6.5px">feb 19</text><text class="axis-label" x="50" y="120" style="font-size:6.5px">ott 19</text><text class="axis-label" x="92" y="120" style="font-size:6.5px">feb 20</text><text class="axis-label" x="134" y="120" style="font-size:6.5px">mag 20</text><text class="axis-label" x="176" y="120" style="font-size:6.5px">nov 20</text>
  </svg>
  <div class="abs text" style="left:24px;width:212px;top:432px">
    <p>Il timore che il digitale ostacoli i rapporti e la socialità dei ragazzi è calato durante il primo lockdown, quando alcune formule di relazione digitale hanno «stupito» per essere in grado di supplire alla mancanza di quelle fisiche ed è diminuita la condanna verso le relazioni a distanza.</p>
  </div>
  <div class="abs text" style="left:255px;right:24px;top:62px">
    <p>La rilevazione successiva, però, ha mostrato che il cambiamento di giudizio è stato temporaneo e non si può ritenere un trend di lungo periodo: a novembre 2020 la paura che le <b>relazioni a distanza deteriorino la socialità</b> dei ragazzi è nuovamente aumentata, tornando al livello pre Covid.</p>
  </div>
  <div class="banner" style="top:124px;left:255px;right:24px;background:var(--purple-soft);font-style:italic">Il Grande Fratello</div>
  <svg class="abs" style="left:255px;top:142px" width="212" height="90" viewBox="0 0 212 90">
    <polyline points="20,64 62,52 106,52 150,28 190,40" fill="none" stroke="#777" stroke-width="1.2" stroke-dasharray="1.5 3" stroke-linecap="round"/>
    <text class="chart-label" x="10" y="78">72%</text><text class="chart-label" x="52" y="46">74%</text><text class="chart-label" x="96" y="66">74%</text><text class="chart-label" x="140" y="22">77%</text><text class="chart-label" x="178" y="34">75%</text>
    <text class="axis-label" x="10" y="88" style="font-size:6.5px">feb 19</text><text class="axis-label" x="50" y="88" style="font-size:6.5px">ott 19</text><text class="axis-label" x="92" y="88" style="font-size:6.5px">feb 20</text><text class="axis-label" x="134" y="88" style="font-size:6.5px">mag 20</text><text class="axis-label" x="176" y="88" style="font-size:6.5px">nov 20</text>
  </svg>
  <div class="abs text" style="left:255px;right:24px;top:240px">
    <p>3 rispondenti su 4 (ovvero 30 milioni di individui, metà della popolazione italiana) sono convinti che <b>alcune organizzazioni sappiano tutto di noi</b>, anche quando non siamo online. Il dato era leggermente aumentato nella primavera del 2020 probabilmente come conseguenza del dibattito sulle capacità dei sistemi di tracciamento nel contrastare la diffusione del contagio ma è rientrato al livello pre Covid.</p>
    <p>Questo aspetto è stato incluso tra gli atteggiamenti di sospetto ma il giudizio negativo potrebbe riguardare solo una parte dei cittadini: altri – di cui tuttavia ignoriamo il numero – potrebbero ritenere che il controllo sociale sia un aspetto positivo del digitale.</p>
  </div>
  <div class="page-foot">La dimensione digitale della vita | DICEMBRE 2021 | @CorvalMeadow2021<div class="page-num" style="background:var(--purple-soft)">PAGE 4</div></div>
</section>

<!-- ===== Le Speranze 1 ===== -->
<section class="page" style="left:83px;top:2202px">
  <div class="page-head">
    <div class="head-icon" style="background:var(--orange)"><svg width="20" height="19" viewBox="0 0 20 19"><polygon points="10,1 12.6,7 19,7.3 14,11.4 15.7,18 10,14.3 4.3,18 6,11.4 1,7.3 7.4,7" fill="none" stroke="#fff" stroke-width="1.5" stroke-linejoin="round"/></svg></div>
    <div class="head-title" style="color:var(--orange)">Le Speranze</div>
  </div>
  <div class="brand-mark"><i></i>Corval Meadow</div>
  <div class="abs text" style="left:24px;right:24px;top:62px">
    <p>Un italiano su due guarda alla diffusione del digitale con un <b>atteggiamento positivo</b>, fiducioso nel fatto che questo fenomeno possa avere un impatto virtuoso su diversi ambiti della vita quotidiana dei cittadini e sulla società. La speranza più diffusa è la semplificazione conseguente al processo di digitalizzazione: il 77% del campione ritiene che il processo di digitalizzazione rende <b>più semplice la vita</b> dei cittadini. Attorno e grazie al digitale si sviluppano inoltre competenze e una <b>generale crescita di conoscenza</b> di cui beneficia tutta la società.</p>
  </div>
  <div class="banner" style="top:128px;background:var(--orange-soft)">Le speranze e le attese</div>
  <div class="bars" style="top:150px">
    <div class="bar-row"><div class="bar-label">la digitalizzazione semplifica la nostra vita di cittadini</div><div class="bar-track"><div class="bar" style="width:78%;background:var(--orange)">78%</div></div></div>
    <div class="bar-row"><div class="bar-label">c'è una generale crescita di competenze e conoscenza grazie al digitale</div><div class="bar-track"><div class="bar" style="width:72%;background:var(--orange)">72%</div></div></div>
    <div class="bar-row"><div class="bar-label">nelle Smart Home con qualità della vita è più elevata</div><div class="bar-track"><div class="bar" style="width:54%;background:var(--orange)">54%</div></div></div>
    <div class="bar-row"><div class="bar-label">nelle Smart City la qualità della vita è più elevata</div><div class="bar-track"><div class="bar" style="width:53%;background:var(--orange)">53%</div></div></div>
    <div class="bar-row"><div class="bar-label">la diffusione online delle notizie rende il sistema dell'info più trasparente…</div><div class="bar-track"><div class="bar" style="width:51%;background:var(--orange)">51%</div></div></div>
    <div class="bar-row"><div class="bar-label">l'applicazione dell'AI ai dati della mia salute mi consente di vivere meglio e più…</div><div class="bar-track"><div class="bar" style="width:47%;background:var(--orange)">47%</div></div></div>
    <div class="bar-row"><div class="bar-label">forme d'informazione e partecipazione digitali miglioreranno il funzionamento…</div><div class="bar-track"><div class="bar" style="width:43%;background:var(--orange)">43%</div></div></div>
    <div class="bar-row"><div class="bar-label">evasione fiscale e lavoro nero calano grazie alla digitalizzazione delle PA</div><div class="bar-track"><div class="bar" style="width:37%;background:var(--orange)">37%</div></div></div>
  </div>
  <div class="abs note" style="left:24px;right:24px;top:230px">Incidenza sul totale campione dei Top2Box di accordo, in una scala a 5 passi (1.017 casi a novembre 2020)</div>
  <div class="abs" style="left:24px;right:24px;top:250px;height:338px;background:var(--peach)"></div>
  <div class="abs text" style="left:34px;right:34px;top:258px">
    <p>Un italiano su due guarda alla diffusione del digitale con un <b>atteggiamento positivo</b>, fiducioso nel fatto che questo fenomeno possa avere un impatto virtuoso su diversi ambiti della vita quotidiana dei cittadini e sulla società. La speranza più diffusa è la semplificazione conseguente al processo di digitalizzazione: il 77% del campione ritiene che il processo di digitalizzazione rende <b>più semplice la vita</b> dei cittadini. Attorno e grazie al digitale si sviluppano inoltre competenze e una <b>generale crescita di conoscenza</b> di cui beneficia tutta la società.</p>
  </div>
  <div class="banner" style="top:319px;background:var(--orange-soft);height:17px;font-size:10px">Il trend dell'indice di speranza</div>
  <svg class="abs" style="left:34px;top:345px" width="423" height="230" viewBox="0 0 423 230">
    <polyline points="40,84 110,104 190,64 275,54 360,64" fill="none" stroke="var(--orange)" stroke-width="1.4" stroke-dasharray="1.5 3" stroke-linecap="round"/>
    <text class="chart-label" x="30" y="100">53%</text><text class="chart-label" x="103" y="122">51%</text><text class="chart-label" x="180" y="58">54%</text><text class="chart-label" x="265" y="48">55%</text><text class="chart-label" x="352" y="80">54%</text>
    <text class="axis-label" x="28" y="195">feb 19</text><text class="axis-label" x="100" y="195">ott 19</text><text class="axis-label" x="178" y="195">feb 20</text><text class="axis-label" x="262" y="195">mag 20</text><text class="axis-label" x="348" y="195">nov 20</text>
    <line x1="15" y1="180" x2="408" y2="180" stroke="#e3c9a8" stroke-width=".6"/>
  </svg>
  <div class="abs note" style="left:24px;right:24px;top:557px">Incidenza sul totale campione dei Top2Box di accordo, in una scala a 5 passi (1.017 casi a novembre 2020)</div>
  <div class="page-foot">La dimensione digitale della vita | DICEMBRE 2021 | @CorvalMeadow2021<div class="page-num" style="background:var(--orange-soft)">PAGE 5</div></div>
</section>

<!-- ===== Le Speranze 2 ===== -->
<section class="page" style="left:634px;top:2202px">
  <div class="page-head">
    <div class="head-icon" style="background:var(--orange)"><svg width="20" height="19" viewBox="0 0 20 19"><polygon points="10,1 12.6,7 19,7.3 14,11.4 15.7,18 10,14.3 4.3,18 6,11.4 1,7.3 7.4,7" fill="none" stroke="#fff" stroke-width="1.5" stroke-linejoin="round"/></svg></div>
    <div class="head-title" style="color:var(--orange)">Le Speranze</div>
  </div>
  <div class="brand-mark"><i></i>Corval Meadow</div>

  <div class="banner" style="top:58px;background:var(--orange-soft)">Il Digitale Semplifica la Vita</div>
  <div class="abs text" style="left:24px;width:250px;top:80px">
    <p><b>Il digitale semplificherà la nostra vita di cittadini</b>»: ne sono convinti circa tre italiani su quattro in un trend che sembrava in diminuzione ma che è tornato a rafforzarsi durante l'emergenza del Covid-19, quando la tecnologia digitale ha mostrato di essere un abilitatore e facilitatore della vita privata, lavorativa e di cittadini nei rapporti con la pubblica amministrazione.</p>
  </div>
  <div class="abs" style="left:300px;right:24px;top:80px"><div class="sub-chart-title">Il digitale semplifica la vita</div></div>
  <svg class="abs" style="left:300px;top:96px" width="167" height="100" viewBox="0 0 167 100">
    <g fill="var(--orange-soft)"><circle cx="16" cy="36" r="11"/><circle cx="48" cy="46" r="11"/><circle cx="80" cy="60" r="11"/><circle cx="112" cy="36" r="11"/><circle cx="144" cy="30" r="11"/></g>
    <g font-family="Barlow" font-size="7" fill="#7a4a10" text-anchor="middle"><text x="16" y="38.5">77%</text><text x="48" y="48.5">75%</text><text x="80" y="62.5">72%</text><text x="112" y="38.5">77%</text><text x="144" y="32.5">78%</text></g>
    <g class="axis-label" style="font-size:6.5px" text-anchor="middle"><text x="16" y="94">feb 19</text><text x="48" y="94">ott 19</text><text x="80" y="94">feb 20</text><text x="112" y="94">mag 20</text><text x="144" y="94">nov 20</text></g>
  </svg>

  <div class="banner" style="top:226px;background:var(--orange-soft)">Informazione più trasparente</div>
  <div class="abs text" style="left:24px;width:250px;top:248px">
    <p>I benefici della diffusione del digitale sulla qualità della vita all'interno delle case e nelle città sono evidenti a circa un italiano su due ma i temi «Smart Home» e «Smart Cities» sembrano aver perso la rilevanza che stavano guadagnando in periodo pre Covid. L'entusiasmo per la <b>democrazia partecipativa</b> e <b>per l'informazione diffusa</b>, con i conseguenti benefici sul funzionamento del sistema democratico, non decolla e anche le aspettative relative all'emersione del «nero» grazie alla digitalizzazione dei processi amministrativi si stanno spegnendo col tempo: ci «crede» poco più di un italiano su tre. In costante crescita invece la convinzione che la diffusione online dell'informazione di attualità abbia reso il sistema nel suo complesso <b>più trasparente</b>.</p>
  </div>
  <div class="abs" style="left:300px;right:24px;top:256px"><div class="sub-chart-title">Informazione più trasparente</div></div>
  <svg class="abs" style="left:300px;top:272px" width="167" height="100" viewBox="0 0 167 100">
    <g fill="var(--orange-soft)"><circle cx="16" cy="60" r="11"/><circle cx="48" cy="56" r="11"/><circle cx="80" cy="52" r="11"/><circle cx="112" cy="46" r="11"/><circle cx="144" cy="40" r="11"/></g>
    <g font-family="Barlow" font-size="7" fill="#7a4a10" text-anchor="middle"><text x="16" y="62.5">48%</text><text x="48" y="58.5">49%</text><text x="80" y="54.5">50%</text><text x="112" y="48.5">52%</text><text x="144" y="42.5">53%</text></g>
    <g class="axis-label" style="font-size:6.5px" text-anchor="middle"><text x="16" y="94">feb 19</text><text x="48" y="94">ott 19</text><text x="80" y="94">feb 20</text><text x="112" y="94">mag 20</text><text x="144" y="94">nov 20</text></g>
  </svg>

  <div class="banner" style="top:416px;background:var(--orange-soft)">Generale Crescita di Competenze</div>
  <div class="abs text" style="left:24px;width:250px;top:438px">
    <p>Una convinzione largamente diffusa è che stiamo vivendo una generale crescita di competenze trainata dal digitale e il Covid-19 ha certamente accelerato questo fenomeno: lo smartworking, la didattica a distanza, le interazione a distanza, gli acquisti online (solo per citare alcuni esempi) sono esperienze che hanno coinvolto gran parte della popolazione e hanno contribuito ad un aumento delle competenze digitali e della conoscenza.</p>
  </div>
  <div class="abs" style="left:300px;right:24px;top:440px"><div class="sub-chart-title">Generale crescita di competenze</div></div>
  <svg class="abs" style="left:300px;top:456px" width="167" height="160" viewBox="0 0 167 160">
    <g fill="var(--orange-soft)"><circle cx="16" cy="70" r="11"/><circle cx="48" cy="76" r="11"/><circle cx="80" cy="68" r="11"/><circle cx="112" cy="66" r="11"/><circle cx="144" cy="62" r="11"/></g>
    <g font-family="Barlow" font-size="7" fill="#7a4a10" text-anchor="middle"><text x="16" y="72.5">69%</text><text x="48" y="78.5">66%</text><text x="80" y="70.5">69%</text><text x="112" y="68.5">71%</text><text x="144" y="64.5">72%</text></g>
    <g class="axis-label" style="font-size:6.5px" text-anchor="middle"><text x="16" y="140">feb 19</text><text x="48" y="140">ott 19</text><text x="80" y="140">feb 20</text><text x="112" y="140">mag 20</text><text x="144" y="140">nov 20</text></g>
  </svg>
  <div class="page-foot">La dimensione digitale della vita | DICEMBRE 2021 | @CorvalMeadow2021<div class="page-num" style="background:var(--orange-soft)">PAGE 6</div></div>
</section>

<!-- ===== Data & Privacy 1 ===== -->
<section class="page" style="left:83px;top:2878px">
  <div class="page-head">
    <div class="head-icon" style="background:var(--navy)"><svg width="18" height="20" viewBox="0 0 18 20"><path d="M9 1 L16 4 V10 C16 14 13 17 9 19 C5 17 2 14 2 10 V4 Z" fill="none" stroke="#fff" stroke-width="1.6"/><rect x="6" y="9" width="6" height="5" fill="#fff"/><path d="M7 9 V7.5 a2 2 0 0 1 4 0 V9" fill="none" stroke="#fff" stroke-width="1.2"/></svg></div>
    <div class="head-title" style="color:var(--navy)">Data &amp; Privacy</div>
  </div>
  <div class="brand-mark"><i></i>Corval Meadow</div>
  <div class="abs text" style="left:24px;right:24px;top:62px">
    <p>L'atteggiamento delle persone di fronte al tema del tracciamento e dell'utilizzo dei dati personali è ambivalente. La popolazione online si divide sostanzialmente in due: chi vive col terrore di essere tracciato e vede un grande pericolo in questa prassi, sia per le conseguenze sulla libertà del singolo individuo che sulla società (il tracciamento è visuto come controllo e manipolazione) e chi, invece – nonostante sia consapevole di alcuni rischi – il ritiene accettabili se paragonati ai benefici ottenuti grazie alla tecnologia. Il rischio più sentito è legato all'utilizzo dei dati personali a fini commerciali, più di un presunto utilizzo dei dati dei cittadini per ridefinire gli equilibri geo-politici tra stati e potenze. Il 58% del campione dichiara però di essere «attrezzato» per ridurre la quantità di dati forniti a sistemi che li utilizzano per fini commerciali e ritiene che questa prassi saranno sempre più diffusa.</p>
  </div>
  <div class="banner" style="top:150px;background:var(--blue-soft)">Timori e consapevolezze</div>
  <div class="bars" style="top:172px">
    <div class="bar-row"><div class="bar-label">nel giro di 3 anni sarà chiaro a tutti che non bisogna dare troppi dati ai sistemi che li usano per fini…</div><div class="bar-track"><div class="bar" style="width:58%;background:var(--navy)">58%</div></div></div>
    <div class="bar-row"><div class="bar-label">quando uso i miei dati, la tecnologia mi dà dei vantaggi reali in cambio dei dati</div><div class="bar-track"><div class="bar" style="width:51%;background:var(--navy)">51%</div></div></div>
    <div class="bar-row"><div class="bar-label">vedo dei pericoli ma i benefici della tecnologia sono tali che per averli posso rinunciare a un po' di…</div><div class="bar-track"><div class="bar" style="width:44%;background:var(--blue-soft)">44%</div></div></div>
    <div class="bar-row"><div class="bar-label">l'equilibrio è giusto: io do un po' di mie informazioni e da' altra parte ricevo benefici in cambio</div><div class="bar-track"><div class="bar" style="width:43%;background:var(--blue-soft)">43%</div></div></div>
    <div class="bar-row"><div class="bar-label">alcuni Stati raccolgono e conoscono il modo di pensare e agire per fare quello che vogliono…</div><div class="bar-track"><div class="bar" style="width:43%;background:var(--blue-soft)">43%</div></div></div>
    <div class="bar-row"><div class="bar-label">più concediamo dati ai sistemi digitali e più, secondo me, si rinuncia a una parte di libertà</div><div class="bar-track"><div class="bar" style="width:40%;background:var(--blue-soft)">40%</div></div></div>
    <div class="bar-row"><div class="bar-label">sono persone che non hanno nulla da nascondere quelle che vogliono dare i loro dati</div><div class="bar-track"><div class="bar" style="width:35%;background:var(--blue-soft)">35%</div></div></div>
  </div>
  <div class="abs note" style="left:24px;right:24px;top:242px">Incidenza sul totale campione dei Top2Box di accordo, in una scala a 5 passi (1.017 casi a novembre 2020)</div>
  <div class="abs" style="left:24px;right:24px;top:262px;height:330px;background:var(--ice)"></div>
  <div class="abs text" style="left:34px;right:34px;top:272px">
    <p>La sensibilità al tema è stabile nel tempo se si esclude il «picco» rilevato a Maggio 2020. Durante la prima ondata di Covid-19 infatti il tema del tracciamento dei dati personali al fine di contenere il virus è stato particolarmente popolare, causando un aumento generalizzato dell'allarme sul tema, allarme poi rientrato nel giro di pochi mesi.</p>
  </div>
  <div class="banner" style="top:318px;background:var(--blue-soft);height:17px;font-size:10px">Il trend dell'attenzione al tema «Data&amp;Privacy»</div>
  <svg class="abs" style="left:34px;top:345px" width="423" height="230" viewBox="0 0 423 230">
    <polyline points="40,120 110,120 190,100 275,60 360,112" fill="none" stroke="var(--orange)" stroke-width="1.4" stroke-dasharray="1.5 3" stroke-linecap="round"/>
    <text class="chart-label" x="30" y="138">44%</text><text class="chart-label" x="103" y="138">44%</text><text class="chart-label" x="180" y="94">46%</text><text class="chart-label" x="265" y="54">50%</text><text class="chart-label" x="352" y="130">45%</text>
    <text class="axis-label" x="28" y="195">feb 19</text><text class="axis-label" x="100" y="195">nov 19</text><text class="axis-label" x="178" y="195">feb 20</text><text class="axis-label" x="262" y="195">mag 20</text><text class="axis-label" x="348" y="195">nov 20</text>
    <line x1="15" y1="180" x2="408" y2="180" stroke="#b7c3e0" stroke-width=".6"/>
  </svg>
  <div class="abs note" style="left:24px;right:24px;top:557px">L'indice di attenzione al tema è ottenuto come media semplice dei Top2Box delle sette voci analizzate</div>
  <div class="page-foot">La dimensione digitale della vita | DICEMBRE 2021 | @CorvalMeadow2021<div class="page-num" style="background:var(--navy)">PAGE 7</div></div>
</section>

<!-- ===== Data & Privacy 2 ===== -->
<section class="page" style="left:634px;top:2878px">
  <div class="page-head">
    <div class="head-icon" style="background:var(--navy)"><svg width="18" height="20" viewBox="0 0 18 20"><path d="M9 1 L16 4 V10 C16 14 13 17 9 19 C5 17 2 14 2 10 V4 Z" fill="none" stroke="#fff" stroke-width="1.6"/><rect x="6" y="9" width="6" height="5" fill="#fff"/><path d="M7 9 V7.5 a2 2 0 0 1 4 0 V9" fill="none" stroke="#fff" stroke-width="1.2"/></svg></div>
    <div class="head-title" style="color:var(--navy)">Data &amp; Privacy</div>
  </div>
  <div class="brand-mark"><i></i>Corval Meadow</div>

  <div class="banner" style="top:58px;background:var(--blue-soft)">Tracciamento per fini commerciali</div>
  <div class="abs text" style="left:24px;width:250px;top:82px">
    <p>Il tema del tracciamento dei dati personali per fini commerciali si conferma in tutte le rilevazioni una pratica fastidiosa per la maggioranza degli intervistati, con una quota variabile tra il 57 e il 62%.</p>
    <p>Si nota però una leggera e progressiva diminuzione dell'attenzione degli italiani su questo aspetto. Forse perché, essendo ormai una prassi consolidata, la si ritiene sempre più inevitabile e sempre meno urgente.</p>
  </div>
  <div class="abs" style="left:300px;right:24px;top:82px"><div class="sub-chart-title">Tracciamento per fini commerciali</div></div>
  <svg class="abs" style="left:300px;top:98px" width="167" height="100" viewBox="0 0 167 100">
    <g fill="var(--blue-soft)"><circle cx="16" cy="42" r="11"/><circle cx="48" cy="36" r="11"/><circle cx="80" cy="42" r="11"/><circle cx="112" cy="50" r="11"/><circle cx="144" cy="48" r="11"/></g>
    <g font-family="Barlow" font-size="7" fill="#fff" text-anchor="middle"><text x="16" y="44.5">60%</text><text x="48" y="38.5">62%</text><text x="80" y="44.5">60%</text><text x="112" y="52.5">57%</text><text x="144" y="50.5">58%</text></g>
    <g class="axis-label" style="font-size:6.5px" text-anchor="middle"><text x="16" y="94">feb 19</text><text x="48" y="94">ott 19</text><text x="80" y="94">feb 20</text><text x="112" y="94">mag 20</text><text x="144" y="94">nov 20</text></g>
  </svg>

  <div class="banner" style="top:226px;background:var(--blue-soft)">La tecnologia toglie, la tecnologia dà</div>
  <div class="abs text" style="left:24px;width:250px;top:250px">
    <p>Come già osservato a livello generale, durante la prima ondata di Covid-19 l'attenzione al tema della privacy è aumentata significativamente e le posizioni degli italiani si sono estremizzate e polarizzate. Se da un lato aumenta il sospetto che i dati personali siano utilizzati ridefinire gli equilibri geo-politici tra Stati e che il tracciamento possa essere un pericolo per la società, dall'altro si nota che l'emergenza Covid ha stimolato un atteggiamento più «benevolo» ed «equilibrato» verso la tecnologia, eliminando alcune resistenze al tracciamento e agevolando l'accettazione del compromesso che per godere dei vantaggi derivanti dalla tecnologia sia necessario rinunciare in parte alle propria privacy.</p>
  </div>
  <div class="abs" style="left:300px;right:24px;top:250px"><div class="sub-chart-title">La tecnologia toglie, la tecnologia dà</div></div>
  <svg class="abs" style="left:300px;top:266px" width="167" height="100" viewBox="0 0 167 100">
    <g fill="var(--blue-soft)"><circle cx="16" cy="44" r="11"/><circle cx="48" cy="48" r="11"/><circle cx="80" cy="54" r="11"/><circle cx="112" cy="28" r="11"/><circle cx="144" cy="46" r="11"/></g>
    <g font-family="Barlow" font-size="7" fill="#fff" text-anchor="middle"><text x="16" y="46.5">45%</text><text x="48" y="50.5">43%</text><text x="80" y="56.5">41%</text><text x="112" y="30.5">52%</text><text x="144" y="48.5">44%</text></g>
    <g class="axis-label" style="font-size:6.5px" text-anchor="middle"><text x="16" y="94">feb 19</text><text x="48" y="94">ott 19</text><text x="80" y="94">feb 20</text><text x="112" y="94">mag 20</text><text x="144" y="94">nov 20</text></g>
  </svg>

  <div class="banner" style="top:416px;background:var(--blue-soft)">Tracciamento per fini geo-politici</div>
  <div class="abs text" style="left:24px;width:250px;top:442px">
    <p>L'effetto Covid sull'atteggiamento delle persone in merito al tema tracciamento e privacy è stato però di breve periodo: già a Novembre 2020, in piena seconda ondata, l'attenzione è tornata al livelli pre pandemia. I livelli che comunque mostravano una diffusa preoccupazione su tutti i piani (geo-politica, società, libertà individuale) accompagnata da una diffusa consapevolezza dell'equilibrio e del bilanciamento (il digitale toglie privacy ma restituisce servizi).</p>
  </div>
  <div class="abs" style="left:300px;right:24px;top:442px"><div class="sub-chart-title">Tracciamento per fini geo-politici</div></div>
  <svg class="abs" style="left:300px;top:458px" width="167" height="150" viewBox="0 0 167 150">
    <g fill="var(--blue-soft)"><circle cx="16" cy="80" r="11"/><circle cx="48" cy="74" r="11"/><circle cx="80" cy="68" r="11"/><circle cx="112" cy="50" r="11"/><circle cx="144" cy="72" r="11"/></g>
    <g font-family="Barlow" font-size="7" fill="#fff" text-anchor="middle"><text x="16" y="82.5">40%</text><text x="48" y="76.5">42%</text><text x="80" y="70.5">44%</text><text x="112" y="52.5">50%</text><text x="144" y="74.5">43%</text></g>
    <g class="axis-label" style="font-size:6.5px" text-anchor="middle"><text x="16" y="128">feb 19</text><text x="48" y="128">ott 19</text><text x="80" y="128">feb 20</text><text x="112" y="128">mag 20</text><text x="144" y="128">nov 20</text></g>
  </svg>
  <div class="page-foot">La dimensione digitale della vita | DICEMBRE 2021 | @CorvalMeadow2021<div class="page-num" style="background:var(--navy)">PAGE 8</div></div>
</section>

</body>
</html>
```